Stout Hearts rescue website

I need a website for my Stout Hearts rescue. We rescue bully breeds from up and down the east coast of the United States and train them as service dogs for people with limited mobility disabilities. I don't want a lot of white space. I want it to be modern and slick and colorful and still look professional. I want it to be different and have a lot of wow factor. I linked a copy of my logo.

Number of Pages Required

5+ page

Font styles to use
Sans Serif

Colors

Designer to choose colors to be used in the design.

Requirements
Must have
• Moving aspects. Blog and ecommerce.
• 1.) Home page
• 2.) Services- something modular
• 3.) About US
• 4.) Blog
• 5.) Application page
• 6.) Donation page
• 7.) Contact Us
Nice to have
• Large Slider of photos on home page
• vertical menu bar
Should not have
• Lots of white space. Dont want it to look like a template or any other site

```html
<!DOCTYPE html>
<html lang="en">
<head>
<meta charset="utf-8">
<title>Stout Hearts – Rescue</title>
<link href="https://fonts.googleapis.com/css2?family=Open+Sans:wght@300;400;600;700;800&family=Rye&display=swap" rel="stylesheet">
<style>
:root{
  --red:#e0002a;
  --red-btn:#e8112d;
  --black:#111111;
  --ink:#333333;
  --muted:#555555;
  --gold:#f5a623;
  --white:#ffffff;
  --light:#f6f6f6;
  --line:#e4e4e4;
}
*{margin:0;padding:0;box-sizing:border-box}
html,body{width:1200px;height:2663px;overflow:hidden}
body{font-family:"Open Sans",Arial,sans-serif;color:var(--ink);background:var(--white);position:relative}

/* hero */
.hero{position:absolute;left:0;top:0;width:1200px;height:740px;overflow:hidden}
.hero-photo{position:absolute;inset:0;background:linear-gradient(180deg,#4d5f74 0%,#6e7f92 35%,#8a8a86 58%,#6b4a32 72%,#8c6d56 86%,#4f4236 100%)}
.brand{position:absolute;left:100px;top:52px;display:flex;align-items:center;gap:10px;color:var(--white);font-weight:800;font-size:22px;line-height:26px}
.brand-dot{width:22px;height:22px;border-radius:50%;background:var(--red)}
.nav{position:absolute;top:58px;left:0;width:1200px;font-size:13px;color:var(--white);text-transform:uppercase}
.nav a{position:absolute;color:var(--white);text-decoration:none}
.nav .active{font-weight:600}
.nav .active::before{content:"";position:absolute;left:0;right:0;top:-12px;height:2px;background:var(--white)}
.cart{position:absolute;left:1047px;top:54px;color:var(--white);font-size:12px;display:flex;align-items:center;gap:4px}
.cart-count{position:absolute;left:14px;top:-6px;width:14px;height:14px;border-radius:50%;background:var(--red);font-size:9px;text-align:center;line-height:14px}
.hero-title{position:absolute;left:0;width:1200px;top:282px;text-align:center;font-family:"Rye",Georgia,serif;font-weight:400;font-size:80px;color:var(--white);line-height:1}
.hero-sub{position:absolute;left:0;width:1200px;top:374px;text-align:center;font-size:11px;font-weight:700;letter-spacing:2px;color:var(--white)}
.hero-btn{position:absolute;left:509px;top:406px;width:181px;height:52px;border:2px solid var(--white);color:var(--white);font-size:20px;font-weight:600;text-align:center;line-height:48px}
.slide-arrow{position:absolute;top:356px;width:48px;height:48px;border-radius:50%;background:rgba(60,60,60,.45)}

/* section heads */
.sec-title{position:absolute;left:0;width:1200px;text-align:center;font-weight:800;font-size:38px;color:#2b2b2b;letter-spacing:1px}
.sec-sub{position:absolute;left:0;width:1200px;text-align:center;font-size:16px;color:var(--muted)}

/* products */
.product{position:absolute;top:907px;width:234px}
.product-photo{width:234px;height:188px;border:1px solid var(--line);background:var(--white);padding:18px}
.product-photo div{width:100%;height:100%;border-radius:6px}
.product-name{margin-top:30px;text-align:center;font-weight:700;font-size:15px;color:#222;text-transform:uppercase;white-space:nowrap}
.product-price{margin-top:12px;text-align:center;font-weight:700;font-size:14px;color:var(--gold)}
.product-actions{margin-top:20px;display:flex;justify-content:center;gap:8px}
.btn-view,.btn-cart{height:31px;width:105px;font-size:11px;text-align:center;line-height:31px;color:var(--white);text-transform:uppercase}
.btn-view{background:var(--black)}
.btn-cart{background:var(--red-btn)}

/* about band */
.about{position:absolute;left:0;top:1310px;width:1200px;height:426px;background:linear-gradient(135deg,#2b2522 0%,#4a3f38 40%,#2e2a27 70%,#3b3632 100%)}
.about-title{position:absolute;left:0;width:1200px;top:104px;text-align:center;font-weight:800;font-size:56px;color:var(--white)}
.about-text{position:absolute;left:160px;width:880px;top:188px;text-align:center;font-weight:300;font-size:20px;line-height:31px;color:#eeeeee}

/* blog */
.blog{position:absolute;left:0;top:1736px;width:1200px;height:587px;background:var(--light)}
.post{position:absolute;top:161px;width:310px;height:244px;overflow:hidden}
.post-photo{position:absolute;inset:0}
.post-title{position:absolute;left:16px;right:40px;color:var(--white);font-weight:800;font-size:17px;line-height:21px;text-transform:uppercase}
.post-date{position:absolute;left:16px;color:var(--white);font-size:11px}
.post-more{position:absolute;left:16px;color:var(--red);font-size:12px;display:flex;align-items:center;gap:6px}
.blog-btn{position:absolute;left:525px;top:474px;width:150px;height:41px;background:var(--red-btn);color:var(--white);font-size:13px;text-align:center;line-height:41px;border-radius:3px}

/* footer */
.footer{position:absolute;left:0;top:2323px;width:1200px;height:340px;background:var(--red);color:var(--white)}
.f-head{position:absolute;top:54px;font-weight:700;font-size:18px}
.f-list{position:absolute;top:95px;list-style:none;font-size:15px;line-height:32px}
.f-divider{position:absolute;top:40px;width:1px;height:222px;background:rgba(255,255,255,.18)}
.f-contact{position:absolute;left:513px;top:95px;font-size:15px;line-height:32px}
.f-contact div{display:flex;align-items:center;gap:6px}
.f-news-text{position:absolute;left:774px;top:88px;font-size:15px}
.f-input{position:absolute;left:776px;top:114px;width:218px;height:38px;background:var(--white);color:#aaa;font-size:11px;line-height:38px;padding-left:16px;letter-spacing:1px}
.f-subscribe{position:absolute;left:996px;top:114px;width:104px;height:38px;background:var(--black);font-weight:700;font-size:14px;text-align:center;line-height:38px}
.social{position:absolute;top:170px;width:38px;height:38px;border-radius:50%;background:var(--white)}
.f-bottom{position:absolute;left:100px;right:100px;top:274px;height:1px;background:rgba(255,255,255,.2)}
.f-copy{position:absolute;left:100px;top:294px;font-size:12px}
.pay{position:absolute;top:296px;height:16px;border-radius:3px;background:rgba(255,255,255,.75)}
</style>
</head>
<body>

<header class="hero">
  <div class="hero-photo" role="img" aria-label="Large dog resting on a gravel beach under a cloudy sky"></div>
  <div class="brand"><span class="brand-dot"></span>Stout Hearts</div>
  <nav class="nav">
    <a class="active" style="left:351px">Home</a>
    <a style="left:431px">Services</a>
    <a style="left:529px">About Us</a>
    <a style="left:634px">Blog</a>
    <a style="left:708px">Application</a>
    <a style="left:831px">Donation</a>
    <a style="left:941px">Contact Us</a>
  </nav>
  <div class="cart">
    <svg width="20" height="18" viewBox="0 0 20 18"><path d="M1 2h3l2.5 9h10l2-7H5.5" fill="none" stroke="#fff" stroke-width="2"/><circle cx="8" cy="15" r="1.6" fill="#fff"/><circle cx="15" cy="15" r="1.6" fill="#fff"/></svg>
    <span class="cart-count">0</span>0.00
  </div>
  <h1 class="hero-title">STOUT HEARTS</h1>
  <p class="hero-sub">We rescue bully breeds from up and down the east coast of the United States</p>
  <div class="hero-btn">LEARN MORE</div>
  <div class="slide-arrow" style="left:20px"><svg width="48" height="48"><path d="M28 14l-10 10 10 10" fill="none" stroke="#ddd" stroke-width="2"/></svg></div>
  <div class="slide-arrow" style="left:1116px"><svg width="48" height="48"><path d="M20 14l10 10-10 10" fill="none" stroke="#ddd" stroke-width="2"/></svg></div>
</header>

<h2 class="sec-title" style="top:788px">OUR PRODUCTS</h2>
<p class="sec-sub" style="top:845px">Quis autem vel eum iure reprehenderit qui in ea voluptate velit esse</p>

<div class="product" style="left:100px">
  <div class="product-photo"><div role="img" aria-label="Pair of metal dog tags on a chain" style="background:linear-gradient(135deg,#f2f2f2,#8a8a8a 55%,#e8e8e8)"></div></div>
  <div class="product-name">Nostrum Exercitationem</div>
  <div class="product-price">FROM $7.99</div>
  <div class="product-actions"><div class="btn-view">View More</div><div class="btn-cart">▪ Add to Cart</div></div>
</div>
<div class="product" style="left:355px">
  <div class="product-photo"><div role="img" aria-label="Woven jute bite tug toy" style="background:linear-gradient(180deg,#fff 30%,#d8bd8e 35%,#c9a877 65%,#fff 70%)"></div></div>
  <div class="product-name">Eiusmod Tempor Incidid</div>
  <div class="product-price">FROM $13.99</div>
  <div class="product-actions"><div class="btn-view">View More</div><div class="btn-cart">▪ Add to Cart</div></div>
</div>
<div class="product" style="left:611px">
  <div class="product-photo"><div role="img" aria-label="Wide black leather dog collar" style="background:radial-gradient(ellipse at center,#2b211c 0%,#3a2c24 45%,#fff 62%)"></div></div>
  <div class="product-name">Dolore Magna Aliqua</div>
  <div class="product-price">FROM $19.99</div>
  <div class="product-actions"><div class="btn-view">View More</div><div class="btn-cart">▪ Add to Cart</div></div>
</div>
<div class="product" style="left:866px">
  <div class="product-photo" style="background:#f3f7fb"><div role="img" aria-label="Colourful bone-shaped dog treats" style="background:linear-gradient(135deg,#f3f7fb,#f2b26a 30%,#f4e06a 50%,#f09a9a 70%,#f3f7fb)"></div></div>
  <div class="product-name">Molestiae Consequatur</div>
  <div class="product-price">FROM $11.99</div>
  <div class="product-actions"><div class="btn-view">View More</div><div class="btn-cart">▪ Add to Cart</div></div>
</div>

<section class="about" role="img" aria-label="Darkened close-up of a resting bulldog's paws">
  <h2 class="about-title">ABOUT STOUT HEARTS</h2>
  <p class="about-text">But I must explain to you how all this mistaken idea of denouncing pleasure and praising pain was born and I will give you a complete account of the system, and expound the actual teachings of the great explorer of the truth, the master-builder of human happiness.</p>
</section>

<section class="blog">
  <h2 class="sec-title" style="top:52px">LATEST BLOG</h2>
  <p class="sec-sub" style="top:104px">Sunt in culpa qui officia deserunt mollit anim id est laborum</p>

  <article class="post" style="left:100px">
    <div class="post-photo" role="img" aria-label="Brown and white bulldog portrait" style="background:linear-gradient(160deg,#6d6a58,#a4764e 45%,#3e3527)"></div>
    <h3 class="post-title" style="top:140px">Dolore Magnam Aliquam Quaerat Voluptatem</h3>
    <div class="post-date" style="top:198px">APRIL 14, 2015</div>
  </article>
  <article class="post" style="left:444px">
    <div class="post-photo" role="img" aria-label="Bowls on a dark wooden table" style="background:linear-gradient(180deg,#2a2a2a,#3a3330 60%,#4a2b25)"></div>
    <h3 class="post-title" style="top:76px;right:70px">Sed Quia Non Numquam Eius Modi Tempora</h3>
    <div class="post-date" style="top:134px">JANUARY 20, 2015</div>
    <div class="post-more" style="top:158px">READ MORE <svg width="12" height="12"><circle cx="6" cy="6" r="6" fill="#e0002a"/><path d="M5 3l3 3-3 3" fill="none" stroke="#fff" stroke-width="1.5"/></svg></div>
  </article>
  <article class="post" style="left:790px">
    <div class="post-photo" role="img" aria-label="Bulldog puppy lying on sand" style="background:linear-gradient(170deg,#8c8a84,#b6ada0 45%,#5c5650)"></div>
    <h3 class="post-title" style="top:140px">Nostrum Exercitationem Ullam Corporis Suscipit</h3>
    <div class="post-date" style="top:198px">APRIL 14, 2015</div>
  </article>

  <div class="blog-btn">VIEW ALL BLOG</div>
</section>

<footer class="footer">
  <div class="f-head" style="left:100px">USEFUL LINKS</div>
  <ul class="f-list" style="left:100px"><li>Home</li><li>Services</li><li>About Us</li><li>Application</li><li>Donation</li></ul>
  <ul class="f-list" style="left:305px"><li>Blog</li><li>Terms of Use</li><li>Contact</li></ul>
  <div class="f-divider" style="left:481px"></div>
  <div class="f-head" style="left:513px">CONTACT INFO</div>
  <div class="f-contact">
    <div>Stout Hearts, Street Address,</div>
    <div>City Name, Country Code.</div>
    <div><svg width="15" height="15"><rect width="15" height="15" rx="2" fill="#fff"/><path d="M4 3c-1 1 0 5 4 8 2 1 3 1 3 0l-1-2-2 1-2-2 1-2z" fill="#e0002a"/></svg>01 2345 6789</div>
    <div><svg width="15" height="12"><rect width="15" height="12" fill="#fff"/><path d="M0 0l7.5 6L15 0" fill="none" stroke="#e0002a" stroke-width="1.5"/></svg>info@domainname.com</div>
  </div>
  <div class="f-divider" style="left:746px"></div>
  <div class="f-head" style="left:774px">SIGN UP FOR NEWSLETTER</div>
  <div class="f-news-text">Please sign up here for latest news</div>
  <div class="f-input">EMAIL ADDRESS</div>
  <div class="f-subscribe">SUBSCRIBE</div>
  <div class="social" style="left:776px"></div>
  <div class="social" style="left:824px"></div>
  <div class="social" style="left:874px"></div>
  <div class="social" style="left:922px"></div>
  <div class="f-bottom"></div>
  <div class="f-copy">© 2018 Stout Hearts.&nbsp; All right reserved&nbsp; Term of Use</div>
  <div class="pay" style="left:916px;width:30px"></div>
  <div class="pay" style="left:954px;width:26px"></div>
  <div class="pay" style="left:988px;width:26px"></div>
  <div class="pay" style="left:1022px;width:22px"></div>
  <div class="pay" style="left:1052px;width:30px"></div>
</footer>

</body>
</html>
```